The Builders Group for Structures and Dwelling Services

The Brochure need to have all the company information and our three products with features and specifications.

1- Sandfall Cube
2- Sandfall Rim
3- Sandfall Arch

We build movable fast build up houses, we are creative and innovative in making designs. we are ECO friendly to the environment. we have an experienced team. We work in Saudi Arabia. we build large number of luxurious houses for hotels and resorts.

Target Market(s)

Hospitality, Tourism, Real State, Saudi Arabia, Mega projects,

Industry/Entity Type

Residential Construction

Font styles to use
Serif

Colors

Designer to choose colors to be used in the design.

Requirements
Must have
• who we are, what we do vision mission values, Products part. Features part, pictures ,our clients our team contact us. Slogan
Nice to have
• it will be decided later
Should not have
• It will be deiced later

```html
<!DOCTYPE html>
<html lang="en">
<head>
<meta charset="utf-8">
<title>The Builders Group – Who We Are Spread</title>
<link rel="stylesheet" href="https://fonts.googleapis.com/css2?family=Lato:ital,wght@0,300;0,400;0,700;0,900;1,400;1,700&display=swap">
<style>
  :root {
    --bg: #e4e4e4;
    --rock-light: #b08562;
    --rock-dark: #5a3f2c;
    --sand: #cfb07a;
    --charcoal: #2f3133;
    --charcoal-deep: #232527;
    --accent-green: #2fbf7a;
    --text-light: #f2f2f2;
    --sky-top: #b9bde8;
    --sky-mid: #9fb6e4;
    --sky-low: #5fa3d6;
    --dome-blue: #3d8fc7;
    --label-bar: #8fc3ec;
    --navy: #1d2d5c;
    --shadow: rgba(0,0,0,0.18);
  }
  * { box-sizing: border-box; margin: 0; padding: 0; }
  html, body { width: 1200px; height: 840px; overflow: hidden; }
  body {
    background: var(--bg);
    font-family: "Lato", sans-serif;
    position: relative;
  }
  .spread {
    position: absolute;
    left: 60px; top: 170px;
    width: 1080px; height: 500px;
    display: flex;
    box-shadow: 0 18px 40px var(--shadow);
  }
  .page { position: relative; width: 540px; height: 500px; overflow: hidden; }

  /* Left page */
  .page--intro { background: var(--charcoal); }
  .intro-photo {
    position: absolute; left: 0; top: 0; width: 100%; height: 100%;
    background:
      linear-gradient(160deg, var(--rock-light) 0%, var(--rock-dark) 38%, var(--sand) 62%, var(--rock-dark) 100%);
  }
  .intro-shade {
    position: absolute; inset: 0;
    background: linear-gradient(120deg, rgba(35,37,39,0) 30%, rgba(35,37,39,0.88) 52%, var(--charcoal-deep) 80%);
  }
  .brand {
    position: absolute; display: flex; align-items: center; gap: 7px;
    color: var(--text-light); font-size: 10px; font-weight: 700; letter-spacing: 0.04em;
  }
  .brand__mark { width: 12px; height: 12px; border: 1.5px solid currentColor; }
  .page--intro .brand { right: 34px; top: 200px; max-width: 170px; line-height: 1.25; }
  .intro-copy {
    position: absolute; right: 34px; top: 250px; width: 290px; color: var(--text-light);
  }
  .intro-copy__title {
    font-size: 26px; font-weight: 300; color: var(--accent-green); letter-spacing: 0.02em; margin-bottom: 12px;
  }
  .intro-copy__title strong { font-weight: 900; }
  .intro-copy p { font-size: 10.5px; line-height: 1.5; margin-bottom: 8px; }

  /* Right page */
  .page--values { background: linear-gradient(180deg, var(--sky-top) 0%, var(--sky-mid) 55%, var(--sky-low) 100%); }
  .values-photo {
    position: absolute; left: 0; bottom: 0; width: 100%; height: 230px;
    background: linear-gradient(180deg, rgba(95,163,214,0) 0%, rgba(61,143,199,0.7) 55%, var(--dome-blue) 100%);
  }
  .page--values .brand { left: 30px; top: 26px; color: #ffffff; }
  .value-block { position: absolute; width: 118px; color: var(--navy); }
  .value-block__label {
    display: block; background: var(--label-bar); padding: 4px 8px;
    font-size: 9.5px; font-weight: 700; text-transform: uppercase; margin-bottom: 10px;
  }
  .value-block p, .value-block li {
    font-size: 9.5px; font-style: italic; line-height: 1.4;
  }
  .value-block ul { list-style: none; }
  .value-block li { padding-left: 10px; position: relative; margin-bottom: 4px; }
  .value-block li::before {
    content: ""; position: absolute; left: 0; top: 5px; width: 4px; height: 4px; border-radius: 50%; background: var(--navy);
  }
  .value-block--vision { left: 30px; top: 92px; }
  .value-block--mission { left: 155px; top: 122px; }
  .value-block--values { left: 280px; top: 152px; }
  .value-block--themes { left: 405px; top: 182px; }
</style>
</head>
<body>
  <main class="spread">
    <section class="page page--intro">
      <div class="intro-photo" role="img" aria-label="Photo of a Sandfall Cube royal suite unit with wooden sign set against desert rock cliffs"></div>
      <div class="intro-shade"></div>
      <div class="brand"><span class="brand__mark"></span><span>THE BUILDERS GROUP</span></div>
      <div class="intro-copy">
        <h1 class="intro-copy__title">WHO <strong>WE ARE?</strong></h1>
        <p>The Builders Group for Structures and Dwelling Services is managed by a professional team of expert Saudi engineers that focuses on bringing innovative, affordable, environmental housing to the country.</p>
        <p>The Builders Group aims to provide a solution for housing complexity in the country, whether it's for construction companies, hospitality or residency. Owning a home should be quick and simple for everyone. We simplified the process of housing to assure that innovation exists to impact your way of living.</p>
      </div>
    </section>

    <section class="page page--values">
      <div class="values-photo" role="img" aria-label="Photo of a row of white geodesic dome tents under a blue sky"></div>
      <div class="brand"><span class="brand__mark"></span><span>THE BUILDERS GROUP</span></div>

      <div class="value-block value-block--vision">
        <span class="value-block__label">Vision</span>
        <p>To inspire and develop the concept of fast Saudi housing solutions.</p>
      </div>
      <div class="value-block value-block--mission">
        <span class="value-block__label">Mission</span>
        <p>To provide a portable housing solutions through an innovative modern design with an expert build up engineers.</p>
      </div>
      <div class="value-block value-block--values">
        <span class="value-block__label">Value Statment</span>
        <p>We believe in boundless potential of Saudi economy. We share the passion for better future, respect the Saudi environment and eco, celebrate, harness the desire for partnership and citizenship and create robust opportunities for housing designs.</p>
      </div>
      <div class="value-block value-block--themes">
        <span class="value-block__label">Strategic Themes</span>
        <ul>
          <li>Promote tourism</li>
          <li>Promote a new experience of camping</li>
          <li>Support hospitality</li>
          <li>Promote construction site communities</li>
          <li>Promote Business Partnering</li>
        </ul>
      </div>
    </section>
  </main>
</body>
</html>
```